Real Estate Investor needs awesome business card design

I invest in real estate, focused on multi-family properties, and I need a business card to hand out to potential partners. I prefer simple, clean designs, but it needs to stand out, so I'd like there to be a bit of red in the design as well.

It should include this information:

Front
Dallin Pecksworth
Real Estate Investor
Direct phone: 502-867-3394
Email: dallinhpecksworth@quillmail.example
Headshot (Picture), I've uploaded a few, just pick the one you think looks best with your design. You can remove the background from the headshot image if it looks better.

Back
The back of the card's design should flow and be congruent with the front. On the back I want to put an inspirational quote or question. There will be different ones depending on the card, so I'll need the original file so I can edit it in the end.

For now, use “The Pessimist Sees Difficulty In Every Opportunity. The Optimist Sees The Opportunity In Every Difficulty.” -Barnaby Ellsworth

Target Market(s)

Investors

Industry/Entity Type

Real Estate

Contact Information for Business Card

Front
Dallin Pecksworth
Real Estate Investor

Back
The back of the card's design should flow and be congruent with the front. On the back I want to put an inspirational quote or question. There will be different ones depending on the card, so I'll need the original file so I can edit it in the end. I've uploaded some EXAMPLES of business cards with quotes on them. Don't copy but feel free to use them as inspiration.

The design will be printed on "ZIB sized" business cards
1039 x 697 pixels
with rounded corners

Font styles to use
Serif
Decorative
Script

Colors
ec1f27

Requirements
Must have
• Headshot, name, and other information in it.
• 1039 x 697 pixels
• Rounded corners
• Clean design that pops. I'm open to see any color background, including black.
• Headshots can be located here: https://www.filecrate.example/sh/8kd2wq7mzt31hvx/BBQTXP4ruf9LmQ0KhcvWx7b?dl=0
Nice to have
• It would be awesome if the design included a personal signature or monogram, but if not I'll get a personal logo developed later and the card redesigned if I think it needs it.
Should not have
• Cluttered design

```html
<!DOCTYPE html>
<html lang="en">
<head>
<meta charset="UTF-8">
<title>Dallin Pecksworth — Business Card</title>
<link href="https://fonts.googleapis.com/css2?family=PT+Serif:wght@400;700&display=swap" rel="stylesheet">
<style>
  :root {
    --page-bg: #d9d9d9;
    --card-white: #ffffff;
    --card-grey: #ececec;
    --band-black: #111111;
    --ink: #1a1a1a;
    --accent-red: #ec1f27;
    --divider: #555555;
  }
  * { margin: 0; padding: 0; box-sizing: border-box; }
  html, body {
    width: 1200px; height: 900px; overflow: hidden;
    background: var(--page-bg);
    font-family: "PT Serif", Georgia, serif;
  }
  .stage {
    width: 1200px; height: 900px;
    display: flex; align-items: center; justify-content: center; gap: 40px;
  }
  .card {
    position: relative;
    width: 540px; height: 362px;
    border-radius: 22px;
    overflow: hidden;
    box-shadow: 0 6px 18px rgba(0,0,0,0.18);
  }

  /* Back */
  .card-back { background: var(--card-grey); }
  .quote-band {
    position: absolute; left: 0; right: 0; top: 96px; height: 128px;
    background: var(--band-black);
    display: flex; flex-direction: column; align-items: center; justify-content: center;
    color: var(--card-white); font-weight: 700; text-transform: uppercase; text-align: center;
    line-height: 1.15;
  }
  .quote-line { font-size: 17px; letter-spacing: 1px; }
  .quote-line.wide { font-size: 20px; letter-spacing: 6px; }
  .quote-author {
    position: absolute; left: 0; right: 0; top: 232px;
    text-align: center; color: var(--accent-red); font-size: 16px; letter-spacing: 0.5px;
  }

  /* Front */
  .card-front { background: var(--card-white); }
  .headshot {
    position: absolute; left: 92px; top: 162px;
    width: 112px; height: 112px; border-radius: 50%;
    border: 3px solid var(--accent-red);
    background: radial-gradient(circle at 50% 40%, #e8d3c4 0%, #c9b3a5 45%, #2b3444 100%);
  }
  .divider {
    position: absolute; left: 232px; top: 150px; width: 1px; height: 130px;
    background: var(--divider);
  }
  .contact { position: absolute; left: 250px; top: 156px; color: var(--ink); }
  .name { font-weight: 700; font-size: 17px; letter-spacing: 1px; text-transform: uppercase; }
  .name .surname { color: var(--accent-red); }
  .role { font-size: 15px; margin-top: 2px; }
  .details { margin-top: 20px; font-size: 13.5px; line-height: 1.55; }
  .detail { display: flex; align-items: center; gap: 8px; }
  .detail svg { width: 11px; height: 11px; flex: none; }
</style>
</head>
<body>
<main class="stage">
  <section class="card card-back" aria-label="Card back">
    <div class="quote-band">
      <span class="quote-line">The Pessimist Sees Difficulty</span>
      <span class="quote-line wide">In Every Opportunity.</span>
      <span class="quote-line">The Optimist Sees The Opportunity</span>
      <span class="quote-line wide">In Every Difficulty.</span>
    </div>
    <p class="quote-author">Barnaby Ellsworth</p>
  </section>

  <section class="card card-front" aria-label="Card front">
    <div class="headshot" role="img" aria-label="Headshot of Dallin Pecksworth"></div>
    <div class="divider"></div>
    <div class="contact">
      <p class="name">Dallin <span class="surname">Pecksworth</span></p>
      <p class="role">Real Estate Investor</p>
      <div class="details">
        <p class="detail">
          <svg viewBox="0 0 24 24" aria-hidden="true"><path fill="#ec1f27" d="M6.6 10.8a15.1 15.1 0 0 0 6.6 6.6l2.2-2.2a1 1 0 0 1 1-.25 11.4 11.4 0 0 0 3.6.57 1 1 0 0 1 1 1V20a1 1 0 0 1-1 1A17 17 0 0 1 3 4a1 1 0 0 1 1-1h3.5a1 1 0 0 1 1 1c0 1.25.2 2.45.57 3.57a1 1 0 0 1-.25 1z"/></svg>
          <span>502-867-3394</span>
        </p>
        <p class="detail">
          <svg viewBox="0 0 24 24" aria-hidden="true"><rect x="2.5" y="5" width="19" height="14" fill="none" stroke="#ec1f27" stroke-width="2.5"/><path d="M3 6l9 7 9-7" fill="none" stroke="#ec1f27" stroke-width="2.5"/></svg>
          <span>dallinhpecksworth@quillmail.example</span>
        </p>
      </div>
    </div>
  </section>
</main>
</body>
</html>
```